Business Card for TVK, logo files already created

Please, can you assist with creating a Business card the TVK graphics which are already listed on www.brinmoretech.example
The business card should be modern and upmarket, textured designs are welcome. Please feel free to express yourself and be very bold with your design.

Target Market(s)

Cyber Security

Industry/Entity Type

Information Technology

Contact Information for Business Card

Company Name
Name
Title
Mobile
Fax or Tel
email
url

Font styles to use
Serif
Sans Serif

Colors
3277b5
85acd3
ffffff

```html
<!DOCTYPE html>
<html lang="en">
<head>
<meta charset="utf-8">
<title>TVK Business Card</title>
<link rel="stylesheet" href="https://fonts.googleapis.com/css2?family=Orbitron:wght@700;900&family=Montserrat:wght@600&family=Arimo:wght@400&display=swap">
<style>
  :root {
    --stage: #e4e6ea;
    --card-white: #ffffff;
    --card-navy: #0d1a48;
    --brand-blue: #1f3f95;
    --rule-grey: #6b6e74;
    --ink-white: #ffffff;
  }
  * { margin: 0; padding: 0; box-sizing: border-box; }
  html, body { width: 1200px; height: 801px; overflow: hidden; }
  body {
    background: var(--stage);
    display: flex;
    align-items: center;
    justify-content: center;
    gap: 40px;
  }
  .card {
    width: 540px;
    height: 310px;
    position: relative;
    box-shadow: 0 6px 18px rgba(0,0,0,0.18);
  }
  .card-front {
    background: var(--card-white);
    display: flex;
    flex-direction: column;
    align-items: center;
    justify-content: center;
  }
  .brand-name {
    font-family: "Orbitron", sans-serif;
    font-weight: 900;
    font-size: 66px;
    line-height: 1;
    color: var(--brand-blue);
    letter-spacing: 1px;
  }
  .company-name {
    font-family: "Orbitron", sans-serif;
    font-weight: 700;
    font-size: 23px;
    line-height: 1;
    color: var(--brand-blue);
    margin-top: 6px;
    letter-spacing: 1px;
  }
  .company-sub {
    display: flex;
    align-items: center;
    gap: 10px;
    width: 260px;
    margin-top: 4px;
    font-family: "Orbitron", sans-serif;
    font-weight: 700;
    font-size: 11px;
    color: var(--rule-grey);
    letter-spacing: 1px;
  }
  .company-sub::before,
  .company-sub::after {
    content: "";
    flex: 1;
    height: 1px;
    background: var(--rule-grey);
  }
  .tagline {
    font-family: "Montserrat", sans-serif;
    font-weight: 600;
    font-size: 11px;
    color: var(--brand-blue);
    letter-spacing: 2px;
    margin-top: 6px;
  }
  .card-back {
    background: var(--card-navy);
    color: var(--ink-white);
  }
  .person {
    position: absolute;
    left: 46px;
    top: 50px;
    font-family: "Orbitron", sans-serif;
    font-weight: 700;
  }
  .person-name { font-size: 17px; letter-spacing: 1px; line-height: 1.1; }
  .person-title { font-size: 11px; letter-spacing: 1px; margin-top: 2px; }
  .contact {
    position: absolute;
    left: 46px;
    bottom: 40px;
    font-family: "Arimo", sans-serif;
    font-size: 12px;
    line-height: 1.55;
    list-style: none;
  }
  .back-brand {
    position: absolute;
    right: 40px;
    bottom: 36px;
    font-family: "Orbitron", sans-serif;
    font-weight: 900;
    font-size: 46px;
    line-height: 1;
    color: var(--ink-white);
    letter-spacing: 1px;
  }
</style>
</head>
<body>
  <section class="card card-front" aria-label="Card front">
    <div class="brand-name">TVK</div>
    <div class="company-name">BRINMORE</div>
    <div class="company-sub">TECHNOLOGIES</div>
    <div class="tagline">INSIGHT - LED CYBER DEFENCE</div>
  </section>

  <section class="card card-back" aria-label="Card back">
    <div class="person">
      <div class="person-name">DANIEL REYES</div>
      <div class="person-title">CEO/FOUNDER</div>
    </div>
    <ul class="contact">
      <li>Tel : 555 203 7741</li>
      <li>Mob : 555 309 4826</li>
      <li>Fax : 555 412 6095</li>
      <li>daniel@brinmoretech.example</li>
      <li>www.brinmoretech.example</li>
    </ul>
    <div class="back-brand">TVK</div>
  </section>
</body>
</html>
```